Retractable banner.
Health Check For Pets
Check for Ear Mites
Skin Health
Fleas & Ticks

A space SERVE BY <NAME OF CLINIC>

Ideally contain pictures of cats and dogs

```html
<!DOCTYPE html>
<html lang="en">
<head>
<meta charset="utf-8">
<title>Health Check For Pets – Roll-up Banner</title>
<link rel="stylesheet" href="https://fonts.googleapis.com/css2?family=Magra:wght@400;700&family=Ropa+Sans&display=swap">
<style>
  :root {
    --stage: #a4a4a4;
    --paper-light: #ffffff;
    --paper-shade: #dcdcdc;
    --teal: #4ba9b6;
    --teal-deep: #3f96a2;
    --magenta: #a8189a;
    --white: #ffffff;
  }
  html, body {
    margin: 0;
    width: 1040px;
    height: 1200px;
    overflow: hidden;
    background: var(--stage);
  }
  .canvas {
    width: 1040px;
    height: 1200px;
    display: flex;
    align-items: center;
    justify-content: center;
  }
  .banner {
    width: 520px;
    height: 1159px;
    display: block;
    box-shadow: 0 6px 24px rgba(0,0,0,0.25);
  }
  .title {
    font-family: "Magra", sans-serif;
    font-weight: 700;
    font-size: 52px;
    fill: var(--teal);
  }
  .brand-name {
    font-family: "Ropa Sans", sans-serif;
    font-size: 28px;
    fill: var(--magenta);
  }
  .provider, .service {
    font-family: "Ropa Sans", sans-serif;
    font-size: 30px;
    fill: var(--white);
  }
</style>
</head>
<body>
<main class="canvas">
  <svg class="banner" viewBox="382 155 498 1110" xmlns="http://www.w3.org/2000/svg">
    <defs>
      <linearGradient id="paper" x1="0" y1="0" x2="0" y2="1">
        <stop offset="0" stop-color="var(--paper-light)"/>
        <stop offset="0.5" stop-color="#ececec"/>
        <stop offset="1" stop-color="var(--paper-shade)"/>
      </linearGradient>
      <linearGradient id="tealFill" x1="0" y1="0" x2="0" y2="1">
        <stop offset="0" stop-color="#55b3c0"/>
        <stop offset="1" stop-color="var(--teal-deep)"/>
      </linearGradient>
      <linearGradient id="catPhoto" x1="0" y1="0" x2="1" y2="1">
        <stop offset="0" stop-color="#7fb7c4"/>
        <stop offset="0.55" stop-color="#c9bfb8"/>
        <stop offset="1" stop-color="#5e5450"/>
      </linearGradient>
      <linearGradient id="dogPhoto" x1="0" y1="0" x2="0" y2="1">
        <stop offset="0" stop-color="#2a2a22"/>
        <stop offset="0.5" stop-color="#d9c7a4"/>
        <stop offset="1" stop-color="#4f8a2c"/>
      </linearGradient>
      <linearGradient id="vetPhoto" x1="0" y1="0" x2="1" y2="1">
        <stop offset="0" stop-color="#f2f2f0"/>
        <stop offset="0.5" stop-color="#3f7fc4"/>
        <stop offset="1" stop-color="#d8d8d8"/>
      </linearGradient>
      <linearGradient id="iconArea" x1="0" y1="0" x2="1" y2="1">
        <stop offset="0" stop-color="#e9d3e6"/>
        <stop offset="1" stop-color="#d2e9ec"/>
      </linearGradient>
    </defs>

    <rect class="banner-ground" x="382" y="155" width="498" height="1110" fill="url(#paper)"/>

    <path class="teal-field" fill="url(#tealFill)"
      d="M880 500 C780 528 560 512 512 540 C470 570 478 624 520 684 C580 770 642 880 690 962 C732 1042 722 1180 716 1265 L880 1265 Z"/>

    <g class="sweep-band" fill="none" stroke-linecap="butt">
      <path stroke="var(--white)" stroke-width="46"
        d="M880 452 C760 520 520 500 440 542 C392 572 402 632 452 692 C522 772 600 882 650 962 C700 1052 692 1180 692 1265"/>
      <path stroke="var(--magenta)" stroke-width="28"
        d="M880 452 C760 520 520 500 440 542 C392 572 402 632 452 692 C522 772 600 882 650 962 C700 1052 692 1180 692 1265"/>
    </g>

    <g class="brand">
      <rect x="410" y="278" width="20" height="20" fill="var(--magenta)"/>
      <text class="brand-name" x="436" y="298" textLength="100" lengthAdjust="spacingAndGlyphs">Pawcare</text>
    </g>

    <text class="title" x="558" y="275" textLength="295" lengthAdjust="spacingAndGlyphs">Health Check</text>
    <text class="title" x="558" y="345" textLength="190" lengthAdjust="spacingAndGlyphs">For Pets</text>

    <g class="photo-frame">
      <circle cx="662" cy="536" r="126" fill="var(--magenta)"/>
      <circle cx="650" cy="524" r="122" fill="var(--white)"/>
      <circle cx="650" cy="524" r="112" fill="url(#catPhoto)" role="img"
        aria-label="Photo of a fluffy cat held by a vet on an examination table"/>
    </g>

    <g class="photo-frame">
      <circle cx="512" cy="834" r="96" fill="var(--magenta)"/>
      <circle cx="502" cy="825" r="92" fill="var(--white)"/>
      <circle cx="502" cy="825" r="84" fill="url(#dogPhoto)" role="img"
        aria-label="Photo of a puppy and a kitten on grass"/>
    </g>

    <g class="photo-frame">
      <circle cx="752" cy="1086" r="116" fill="var(--magenta)"/>
      <circle cx="740" cy="1074" r="114" fill="var(--white)"/>
      <circle cx="740" cy="1074" r="104" fill="url(#vetPhoto)" role="img"
        aria-label="Photo of a vet listening to a dog with a stethoscope"/>
    </g>

    <text class="provider" x="518" y="700" textLength="339" lengthAdjust="spacingAndGlyphs">Provided By Name of Clinic</text>
    <g class="services">
      <text class="service" x="598" y="762" textLength="259" lengthAdjust="spacingAndGlyphs">• Check for Ear Mites</text>
      <text class="service" x="697" y="814" textLength="160" lengthAdjust="spacingAndGlyphs">• Skin Health</text>
      <text class="service" x="677" y="866" textLength="180" lengthAdjust="spacingAndGlyphs">• Fleas &amp; Ticks</text>
    </g>

    <rect class="illustration-area" x="398" y="966" width="222" height="258" rx="18"
      fill="url(#iconArea)" role="img"
      aria-label="Illustration of a stethoscope with a paw print at its end"/>
  </svg>
</main>
</body>
</html>
```